I need professional letterhead for an attorney. I already have my logo (attached). I currently have a project going to get business cards. I would like the letterhead to be classy. It is very important that this letterhead be in a format that I can import it into Microsoft Word 2013. I plan on importing this into Word so I can type my documents directly onto it and electronically send the finished documents to my clients. Thank you very much.

Industry/Entity Type

Attorney

Requirements
Must have
• Here is my info. Please put it all on there:
• Dwight R. Mallory Attorney At Law
• 48613 Brackwell Crescent
• St. Louis, MO 63047
• Telephone: 314-596-2043
• Fax: 800-627-4915
• Email: Dwight@RivermarkWills.com
• Also, I need the ability to import this final design into Microsoft Word 2013 so that I can type directly onto it. I believe I can do that if you hand it over to me as a JPG and a PDF in addition to the other formats. Then I should be able to import it into Word.

```html
<!DOCTYPE html>
<html lang="en">
<head>
<meta charset="utf-8">
<title>Rivermark Wills Planning LLC — Letterhead</title>
<link href="https://fonts.googleapis.com/css2?family=Open+Sans:wght@400;600&display=swap" rel="stylesheet">
<style>
  :root {
    --brand-blue: #1f6fb5;
    --ink: #222222;
    --muted: #555555;
    --rule-grey: #bfbfbf;
    --watermark: rgba(120, 130, 140, 0.08);
    --paper: #ffffff;
  }
  * { box-sizing: border-box; margin: 0; padding: 0; }
  html, body { width: 849px; height: 1200px; overflow: hidden; background: var(--paper); }
  .letterhead {
    position: relative;
    width: 849px;
    height: 1200px;
    background: var(--paper);
    font-family: "Open Sans", Arial, sans-serif;
    color: var(--ink);
    overflow: hidden;
  }

  .brand {
    position: absolute;
    top: 46px;
    right: 60px;
    display: flex;
    align-items: center;
    gap: 12px;
  }
  .brand-dot {
    width: 44px; height: 44px;
    border-radius: 50%;
    background: var(--brand-blue);
    flex: none;
  }
  .brand-name {
    font-size: 22px;
    font-weight: 400;
    color: var(--brand-blue);
    line-height: 1.2;
  }
  .brand-name span { display: block; }

  .frame-top {
    position: absolute;
    left: 180px; top: 132px;
    width: 610px; height: 3px;
    background: var(--brand-blue);
  }
  .frame-side {
    position: absolute;
    left: 180px; top: 132px;
    width: 3px; height: 910px;
    background: var(--brand-blue);
  }

  .watermark {
    position: absolute;
    left: 210px; top: 660px;
    transform: rotate(-38deg);
    transform-origin: left top;
    font-size: 46px;
    font-weight: 400;
    color: var(--watermark);
    white-space: nowrap;
    pointer-events: none;
  }

  .sender {
    position: absolute;
    left: 30px; top: 262px;
    width: 140px;
  }
  .sender-name {
    font-size: 12px;
    font-weight: 600;
    color: var(--brand-blue);
    text-transform: uppercase;
  }
  .sender-title { font-size: 9px; color: var(--muted); margin-top: 2px; }
  .contact-list { list-style: none; margin-top: 40px; }
  .contact-item { margin-bottom: 24px; }
  .contact-icon { display: block; width: 12px; height: 12px; margin: 0 0 8px 40px; fill: var(--brand-blue); }
  .contact-value { font-size: 10.5px; color: var(--ink); }

  .footer-rule {
    position: absolute;
    left: 50px; right: 50px; top: 1118px;
    height: 1px; background: var(--rule-grey);
  }
  .footer-address {
    position: absolute;
    left: 0; right: 0; top: 1146px;
    text-align: center;
    font-size: 12px;
    color: var(--ink);
  }
</style>
</head>
<body>
<main class="letterhead">
  <header class="brand">
    <span class="brand-dot" aria-hidden="true"></span>
    <div class="brand-name">
      <span>Rivermark Wills</span>
      <span>Planning LLC</span>
    </div>
  </header>

  <div class="frame-top" aria-hidden="true"></div>
  <div class="frame-side" aria-hidden="true"></div>

  <div class="watermark" aria-hidden="true">Rivermark Wills Planning LLC</div>

  <aside class="sender">
    <p class="sender-name">Dwight R. Mallory</p>
    <p class="sender-title">Attorney At Law</p>
    <ul class="contact-list">
      <li class="contact-item">
        <svg class="contact-icon" viewBox="0 0 24 24" aria-label="Telephone"><path d="M6.6 10.8a15.1 15.1 0 0 0 6.6 6.6l2.2-2.2c.3-.3.7-.4 1-.2 1.1.4 2.3.6 3.6.6.6 0 1 .4 1 1V20c0 .6-.4 1-1 1A17 17 0 0 1 3 4c0-.6.4-1 1-1h3.5c.6 0 1 .4 1 1 0 1.3.2 2.5.6 3.6.1.3 0 .7-.2 1z"/></svg>
        <span class="contact-value">314-596-2043</span>
      </li>
      <li class="contact-item">
        <svg class="contact-icon" viewBox="0 0 24 24" aria-label="Fax"><path d="M6 2h9l3 3v5H6zM3 11h18a1 1 0 0 1 1 1v7a1 1 0 0 1-1 1h-3v-4H6v4H3a1 1 0 0 1-1-1v-7a1 1 0 0 1 1-1zm5 7h8v4H8z"/></svg>
        <span class="contact-value">800-627-4915</span>
      </li>
      <li class="contact-item">
        <svg class="contact-icon" viewBox="0 0 24 24" aria-label="Email"><path d="M2 5h20v14H2zm2 2v.5l8 5.5 8-5.5V7l-8 5.5z"/></svg>
        <span class="contact-value">Dwight@RivermarkWills.com</span>
      </li>
    </ul>
  </aside>

  <div class="footer-rule" aria-hidden="true"></div>
  <footer class="footer-address">48613 Brackwell Crescent St. Louis, MO 63047</footer>
</main>
</body>
</html>
```